WordPress Blog/Website for Athlete Focused Sports Marketing Agency

WordPress Website that Serves two primary purposes:

1) Company Information Website which showcases organization's capabilities and work

2) Highlights, Showcases and Displays key information for athlete clients, aggregates all of the content they are creating(mostly social) and is a key portal for publishing press releases, news updates and more.

Key Criteria for Success:

Easily Updatable
Easy to Navigate
Clean Design that follows the function/form of the organization's brand identity while also incorporating the identity of the athletes.

Supporting Documentation:**These files are also uploaded and attached to this project description**
Creative Brief: https://files.briskhollow.net/a/lanternmoor.com/file/d/7KxR2mTqWvB9pLnYcHsDfJgZaQe/edit?usp=sharing
Logo Files/Designs are attached. Color Palette can be adjusted as necessary.

WireFrame: (Please use your own judgement and creative liberty's to make something that is a lot better then what I came up with):
https://files.briskhollow.net/file/d/7KxR2mTqWvB9pXtNbVcMwQrLsKy/edit?usp=sharing

Current Website(Incomplete): www.lanternmoor.com

Thanks!

Industry/Entity Type

It Company

Requirements
Must have
• Social Media Integration: A social feed that aggregates content across all channels for multiple users(all of my athletes)

"News=Blog" Portal that serves as the primary engine for the page's content

Professional Look and Design- it should look like a website, not a blog.

```html
<!DOCTYPE html>
<html lang="en">
<head>
<meta charset="utf-8">
<title>Lantern &amp; Moor</title>
<link href="https://fonts.googleapis.com/css2?family=Varela+Round&family=PT+Sans:wght@400;700&family=PT+Sans+Narrow&display=swap" rel="stylesheet">
<style>
:root{
  --orange:#f67a10;
  --orange-deep:#e76a00;
  --charcoal:#3a3a3a;
  --ink:#2b2b2b;
  --page:#f2f2f2;
  --card:#e7e7e7;
  --white:#ffffff;
}
*{margin:0;padding:0;box-sizing:border-box}
html,body{width:1200px;height:1032px;overflow:hidden}
body{background:radial-gradient(ellipse at 50% 40%,#fafafa 0%,var(--page) 70%);font-family:"Varela Round",sans-serif;color:var(--ink);position:relative}
.abs{position:absolute}

.brand{left:110px;top:28px;display:flex;align-items:center;gap:12px}
.brand-dot{width:82px;height:82px;border-radius:50%;background:var(--charcoal);border:4px solid var(--orange)}
.brand-name{font-family:"Varela Round",sans-serif;color:var(--orange);font-size:46px;letter-spacing:-0.5px}

.main-nav{left:566px;top:57px;display:flex;font-family:"PT Sans",sans-serif;font-size:15px;text-transform:uppercase}
.main-nav a{display:block;height:36px;line-height:36px;color:#444;text-decoration:none;padding:0 14px;margin-right:11px}
.main-nav a.active{background:var(--orange);color:var(--white);width:71px;text-align:center;padding:0}
.main-nav a:nth-child(3){margin-right:15px}
.main-nav a:nth-child(4){margin-right:16px}

.title-band{left:110px;top:128px;width:981px;height:45px;background:var(--charcoal);border-radius:3px}
.title-tag{left:125px;top:146px;width:799px;height:47px;background:var(--orange);border-radius:3px;color:var(--white);font-size:27px;line-height:44px;padding-left:22px;letter-spacing:0.5px}

.hero-photo{left:680px;top:208px;width:405px;height:440px;background:radial-gradient(ellipse at 55% 45%,#f08a3a 0%,#f6c7a0 40%,rgba(250,250,250,0) 72%)}

.feature-dot{left:133px;top:323px;width:80px;height:80px;border-radius:50%;background:var(--charcoal);border:4px solid var(--orange);box-shadow:0 0 0 3px var(--white) inset}
.feature-head{left:180px;top:336px;width:494px;height:56px;background:var(--orange);padding-left:44px;font-size:27px;line-height:56px;letter-spacing:1px;color:var(--white)}
.feature-head strong{color:var(--ink);font-weight:700}
.feature-text{left:140px;top:423px;width:550px;font-size:16px;line-height:24px;color:#333}
.read-more{left:555px;top:556px;color:var(--orange-deep);font-size:15.5px;text-decoration:underline;letter-spacing:0.5px}

.service{top:670px;width:230px;height:222px;background:var(--card);text-align:center}
.service-icon{width:61px;height:61px;border-radius:50%;background:#1c1c1c;margin:18px auto 0;display:flex;align-items:center;justify-content:center}
.service h3{font-weight:400;color:var(--orange);font-size:17.5px;margin-top:14px}
.service p{font-family:"PT Sans Narrow",sans-serif;font-size:13px;line-height:22px;color:#222;padding:0 12px;margin-top:4px}
.service p b{color:var(--orange-deep)}

.footer-band{left:112px;top:940px;width:974px;height:58px;background:#44484b}
.footer-box{left:130px;top:953px;width:738px;height:55px;background:var(--orange-deep);color:var(--white);font-family:"PT Sans",sans-serif;padding:10px 0 0 20px}
.footer-links{display:flex;font-size:12.5px;font-weight:700}
.footer-links span{margin:0 21px}
.footer-copy{font-family:Arial,sans-serif;font-size:11px;margin-top:5px;padding-left:1px}
.footer-brand{left:882px;top:948px;display:flex;align-items:center;gap:6px}
.footer-brand .brand-dot{width:42px;height:42px;border-width:2px}
.footer-brand .brand-name{font-size:25px}
</style>
</head>
<body>
<div class="abs brand"><div class="brand-dot"></div><div class="brand-name">Lantern &amp; Moor</div></div>

<nav class="abs main-nav">
  <a class="active" href="#">Home</a><a href="#">What We Do</a><a href="#">Athletes</a><a href="#">Gallery</a><a href="#">Contact Us</a>
</nav>

<div class="abs title-band"></div>
<div class="abs title-tag">Lantern Avenue to Moor Avenue- A Full Service Agency</div>

<div class="abs hero-photo" role="img" aria-label="Photo of an American football player in an orange and white uniform crouched in a three-point stance"></div>

<div class="abs feature-head"><strong>Product Strategy</strong> &amp; Launches</div>
<div class="abs feature-dot"></div>
<p class="abs feature-text">Think ‘athlete representatives who spent their careers managing some simply dummy text of the printing and typesetting industry. Lorem Ipsum has been the industry's standard of the world’s biggest brands and sponsoring athletes themselves’. We are individuals who build brands, lives with their athletes..</p>
<a class="abs read-more" href="#">Read More &gt;&gt;</a>

<section class="abs service" style="left:114px">
  <div class="service-icon"><svg width="34" height="22" viewBox="0 0 34 22" fill="#fff"><circle cx="9" cy="6" r="4"/><circle cx="25" cy="6" r="4"/><circle cx="17" cy="5" r="5"/><path d="M1 21c0-6 4-9 8-9s6 2 6 2l-2 7zM33 21c0-6-4-9-8-9s-6 2-6 2l2 7zM8 22c0-7 4-11 9-11s9 4 9 11z"/></svg></div>
  <h3>Athlete Brand Building</h3>
  <p>If a business does not continue to provide for the greater good, regardless of whether or not the business is profit-able, the business is a failure <b>&gt;</b></p>
</section>
<section class="abs service" style="left:362px">
  <div class="service-icon"><svg width="28" height="28" viewBox="0 0 28 28" fill="none" stroke="#fff" stroke-width="3"><path d="M5 11a10 10 0 0 1 17-5"/><path d="M23 17a10 10 0 0 1-17 5"/><path d="M19 3l4 3-4 3" fill="#fff"/><path d="M9 25l-4-3 4-3" fill="#fff"/></svg></div>
  <h3 style="margin-top:17px">Lifestyle &amp; Sports</h3>
  <p>A business's success should not be determined by how big it is or how fast it is growing, but instead by its ability to optimally provide its services <b>&gt;</b></p>
</section>
<section class="abs service" style="left:609px">
  <div class="service-icon"><svg width="26" height="26" viewBox="0 0 26 26" fill="none" stroke="#fff" stroke-width="3.5"><circle cx="10" cy="10" r="7"/><path d="M15 15l8 8" stroke-linecap="round"/></svg></div>
  <h3 style="margin-top:18px">Athlete Building</h3>
  <p>Providing a transparent view of business activities enforces company honesty to its shareholders, employees and customers <b>&gt;</b></p>
</section>
<section class="abs service" style="left:855px">
  <div class="service-icon"><svg width="26" height="22" viewBox="0 0 26 22" fill="#fff"><ellipse cx="11" cy="8" rx="10" ry="7"/><path d="M4 13l-2 5 6-3z"/><ellipse cx="17" cy="12" rx="8" ry="5.5" stroke="#1c1c1c" stroke-width="1.5"/></svg></div>
  <h3 style="margin-top:19px">Lifestyle &amp; Sports</h3>
  <p>There should always be a pool of equity available for anyone to wants to own a piece of the business. Ownership creates loyalty <b>&gt;</b></p>
</section>

<div class="abs footer-band"></div>
<footer class="abs footer-box">
  <div class="footer-links">Home<span>|</span>What We Do<span>|</span>Athletes<span>|</span>Gallery<span>|</span>Contact Us</div>
  <div class="footer-copy">Copyright (C) 2012 - Lantern &amp; Moor. All rights reserved.</div>
</footer>
<div class="abs footer-brand"><div class="brand-dot"></div><div class="brand-name">Lantern &amp; Moor</div></div>
</body>
</html>
```